Web Design Project for velbrook

We are looking for a sleek and sophisticated website design for our already developed web-based gallery management software application. Here is a link to our web-app: http://www.vel-brook.co

You will login on the main page and then we would like to include all of the information on the PDF that I am providing below (it outlines what?, where?, why? who? and how much?). Basically, we need a home page, about page, and a pricing page, as well as a sign up page that should be navigable from the upper right hand corner of the site where the sign in/sign up would be located. Also, our 3 tenets are that the software program is "attractive, accessible, and affordable", which might need to be somehow incorporated. There are a few websites that we would like for you to take inspiration from listed below:

https://tidemoxen.com (for homepage)
https://plumwovenly.com (for homepage/pricing page/etc)
https://tidemoxen.com/tour (for a tour of how the product works)

We are currently having a logo designed and will share that as soon as it is available! Also, let us know if you need photos/screen shots, as we can provide them.

Thanks!

Reason: Extending deadline as we are just now getting designs we would like to see fully developed.

Target Market(s)

art galleries, artists, art collectors, art consultants, museums

Industry/Entity Type

Software

Requirements
Must have
• Home page
About page (or tour through the app)
Pricing page
Sign up page (the more click-throughs to signing up the better)

```html
<!DOCTYPE html>
<html lang="en">
<head>
<meta charset="utf-8">
<title>velbrook — Gallery Management Made Easy</title>
<link rel="stylesheet" href="https://fonts.googleapis.com/css2?family=Source+Sans+3:ital,wght@0,300;0,400;0,600;1,400&family=PT+Sans:wght@400;700&family=Open+Sans:wght@400;700&display=swap">
<style>
:root{
  --green:#44a047;
  --green-dark:#327d35;
  --green-deep:#1f4d21;
  --orange:#f7931e;
  --orange-dark:#e9780c;
  --ink:#333;
  --grey:#777;
  --line:#e3e3e3;
  --footer:#1c1c1c;
  --footer-top:#2b2b2b;
}
*{margin:0;padding:0;box-sizing:border-box}
html,body{width:714px;height:1200px;overflow:hidden;background:#fff}
body{position:relative;font-family:"Source Sans 3",sans-serif;color:var(--ink)}
.abs{position:absolute}

/* header */
.site-header{position:absolute;left:0;top:0;width:714px;height:69px;background:linear-gradient(#fafafa,#fff)}
.logo{position:absolute;left:58px;top:24px;font-size:24px;font-weight:300;color:#555;letter-spacing:-.3px}
.logo-badge{position:absolute;left:166px;top:28px;background:var(--green);color:#fff;font-size:12px;padding:2px 7px;border-radius:2px}
.main-nav{position:absolute;left:300px;top:33px;display:flex;font-family:"PT Sans",sans-serif;font-size:11.5px;color:#444;letter-spacing:.3px}
.main-nav span{padding:0 12px;border-left:1px solid #bbb;line-height:13px}
.main-nav span:first-child{border-left:0;padding-left:4px}
.btn{position:absolute;color:#fff;font-family:"Open Sans",sans-serif;font-size:9px;text-align:center;border-radius:2px}
.btn-signin{left:553px;top:30px;width:68px;height:21px;line-height:21px;background:linear-gradient(var(--green),var(--green-dark))}
.btn-signup{left:610px;top:30px;width:46px;height:21px;line-height:21px;background:linear-gradient(#fba53a,var(--orange-dark))}

/* hero */
.hero{position:absolute;left:0;top:69px;width:714px;height:238px;background:linear-gradient(#4ea852,#3d8f40);overflow:hidden}
.hero-title{position:absolute;left:62px;top:46px;font-family:"Open Sans",sans-serif;color:#fff;font-size:22px;line-height:25px;font-weight:400}
.hero-text{position:absolute;left:62px;top:103px;color:#e4f3e4;font-size:12px;line-height:16px;font-weight:300;width:230px}
.hero-cta{position:absolute;left:62px;top:142px;width:100px;height:25px;line-height:25px;background:var(--green-deep);color:#fff;font-size:8.5px;font-weight:700;font-family:"Open Sans",sans-serif;text-align:center;border-radius:2px}
.hero-dots{position:absolute;left:62px;top:176px;display:flex;gap:3px}
.hero-dots i{width:8px;height:8px;border-radius:50%;background:#c6e0c6}
.app-panel{position:absolute;left:310px;top:21px;width:344px;height:230px;background:#8fc791;border-radius:3px;padding:5px}
.app-window{background:#fff;height:100%;padding:6px 8px;font-family:Arial,sans-serif}
.app-title{font-size:12px;font-weight:700;color:#222}
.app-tools{display:flex;justify-content:space-between;font-size:4.5px;color:#555;margin-top:1px}
.app-tools b{display:inline-block;width:72px;height:8px;border:1px solid #ccc;vertical-align:middle;margin-left:2px}
.app-table{width:100%;border-collapse:collapse;margin-top:7px;font-size:4.5px;color:#333}
.app-table th{text-align:left;font-weight:700;border-bottom:1px solid #ccc;padding:2px 3px;background:#f3f3f3}
.app-table td{border-bottom:1px solid #eaeaea;padding:0 3px;height:22.6px}
.thumb{display:block;width:14px;height:12px;border:1px solid #ccc}
.qty{display:inline-block;width:7px;height:5px;border-radius:3px;background:#2f7bbf}
.opt{display:inline-block;border:1px solid #bbb;padding:1px 3px;border-radius:2px}

/* intro */
.intro-title{position:absolute;left:0;top:335px;width:714px;text-align:center;font-size:17px;color:#333}
.intro-text{position:absolute;left:90px;top:360px;width:534px;text-align:center;font-size:9.5px;line-height:13px;color:#777;font-weight:300}
.rule{position:absolute;left:62px;width:576px;height:1px;background:var(--line)}
.soft-rule{position:absolute;left:80px;width:560px;height:14px;background:radial-gradient(ellipse at center,rgba(0,0,0,.05),rgba(0,0,0,0) 70%)}

.feature-title{position:absolute;font-size:15px;color:#333}
.feature-text{position:absolute;font-size:7.8px;line-height:12.8px;color:#888;font-weight:300}
.feature-text p+p{margin-top:8px}
.art{position:absolute}

.col-title{position:absolute;top:820px;font-size:14px;color:#333}
.col-text{position:absolute;top:844px;width:180px;font-size:7.8px;line-height:13px;color:#888;font-weight:300}
.col-text p+p{margin-top:8px}
.btn-more{position:absolute;top:940px;width:64px;height:21px;line-height:21px;background:linear-gradient(#fba53a,var(--orange-dark));color:#fff;font-size:7.5px;text-align:center;border-radius:2px;font-family:"Open Sans",sans-serif}
.quote-photo{position:absolute;left:468px;top:843px;width:54px;height:53px;border:1px solid #ddd;background:linear-gradient(#eee,#d9c4ad)}
.quote-text{position:absolute;left:528px;top:842px;width:135px;font-size:7.8px;line-height:13px;font-style:italic;color:#666}
.quote-author{position:absolute;left:528px;top:912px;font-size:7.8px;color:#444}

/* footer */
.site-footer{position:absolute;left:0;top:1003px;width:714px;height:197px;background:linear-gradient(var(--footer-top),#0f0f0f)}
.foot-col{position:absolute;top:27px;color:#e6e6e6;font-size:7.8px}
.foot-col h4{font-weight:400;font-size:10px;margin-bottom:5px;color:#fff}
.foot-col li{list-style:none;line-height:16px}
.foot-col .ico{display:inline-block;width:10px;height:10px;border-radius:50%;border:1.5px solid #eee;vertical-align:middle;margin-right:5px}
.foot-col .social li{line-height:19px}
.foot-sep{position:absolute;top:28px;width:1px;height:80px;background:#444}
.foot-rule{position:absolute;left:80px;top:152px;width:560px;height:1px;background:#333}
.copyright{position:absolute;left:0;top:166px;width:714px;text-align:center;font-size:7.5px;color:#999}
</style>
</head>
<body>

<header class="site-header">
  <div class="logo">velbrook</div>
  <div class="logo-badge">Beta</div>
  <nav class="main-nav"><span>HOME</span><span>ABOUT</span><span>WHAT WE DO</span><span>BLOG</span></nav>
  <a class="btn btn-signin" style="width:47px">Sign In</a>
  <a class="btn btn-signup">Sign Up</a>
</header>

<section class="hero">
  <h1 class="hero-title">Gallery Management<br>Made Easy</h1>
  <p class="hero-text">velbrook is the simplest way to manage your gallery in the cloud</p>
  <a class="hero-cta">REQUEST FREE TRIAL</a>
  <div class="hero-dots"><i></i><i></i><i></i><i></i></div>

  <div class="app-panel">
    <div class="app-window">
      <div class="app-title">Artwork List</div>
      <div class="app-tools"><span>10 ▾ records per page</span><span>Search:<b></b></span></div>
      <table class="app-table">
        <thead><tr><th>Image</th><th>Name</th><th>Artist</th><th>Width</th><th>Height</th><th>Quantity</th><th>Action</th></tr></thead>
        <tbody>
          <tr><td><i class="thumb" role="img" aria-label="Artwork thumbnail" style="background:#b9c6a8"></i></td><td>Faded Dawn</td><td>Oren Valdt</td><td>48</td><td>48</td><td><i class="qty"></i></td><td><span class="opt">⚙ Options</span></td></tr>
          <tr><td><i class="thumb" role="img" aria-label="Artwork thumbnail" style="background:#c8cfa0"></i></td><td>Tempest</td><td>Oren Valdt</td><td>60</td><td>36</td><td><i class="qty"></i></td><td><span class="opt">⚙ Options</span></td></tr>
          <tr><td><i class="thumb" role="img" aria-label="Artwork thumbnail" style="background:#d2c79a"></i></td><td>Sienna Spring</td><td>Oren Valdt</td><td>36</td><td>36</td><td><i class="qty"></i></td><td><span class="opt">⚙ Options</span></td></tr>
          <tr><td><i class="thumb" role="img" aria-label="Artwork thumbnail" style="background:#b7c9c0"></i></td><td>Coastal View</td><td>Oren Valdt</td><td>36</td><td>36</td><td><i class="qty"></i></td><td><span class="opt">⚙ Options</span></td></tr>
          <tr><td><i class="thumb" role="img" aria-label="Artwork thumbnail" style="background:#bfb98a"></i></td><td>Washed Vista</td><td>Oren Valdt</td><td>48</td><td>36</td><td><i class="qty"></i></td><td><span class="opt">⚙ Options</span></td></tr>
          <tr><td><i class="thumb" role="img" aria-label="Artwork thumbnail" style="background:#9a5a36"></i></td><td>Refuge</td><td>Lise Marrow</td><td>38</td><td>30</td><td><i class="qty"></i></td><td><span class="opt">⚙ Options</span></td></tr>
          <tr><td><i class="thumb" role="img" aria-label="Artwork thumbnail" style="background:#7a1f1a"></i></td><td>Trust</td><td>Lise Marrow</td><td>17</td><td>22</td><td><i class="qty"></i></td><td><span class="opt">⚙ Options</span></td></tr>
        </tbody>
      </table>
    </div>
  </div>
</section>

<h2 class="intro-title">Mauris vel lacus vitae felis vestibulum volutpa</h2>
<p class="intro-text">Suspendisse quam leo, molestie sed, luctus quis, feugiat in, pede. Fusce tellus. Sed metus augue, convallis et, vehicula ut, pulvinar eu, ante. Integer orci tellus, tristique vitae, consequat nec, porta vel, lectus. Nulla sit amet diam. Duis non nunc.</p>
<div class="rule" style="top:411px"></div>

<h3 class="feature-title" style="left:64px;top:430px">What is Velbrook?</h3>
<div class="feature-text" style="left:64px;top:452px;width:314px">
  <p>Phasellus felis dolor, scelerisque a, tempus eget, lobortis id, libero. Donec scelerisque leo ac risus. Praesent sit amet est. In dictum, dolor eu dictum porttitor, enim felis viverra mi, eget luctus massa purus quis odio. Etiam nulla massa, pharetra facilisis, volutpat in, imperdiet sit amet, sem. Aliquam nec erat at purus cursus interdum</p>
  <p>Vestibulum ligula augue, bibendum accumsan, vestibulum ut, commodo a, mi. Morbi ornare gravida elit. Integer congue, augue et malesuada iaculis, ipsum dui aliquet felis</p>
</div>
<div class="art" role="img" aria-label="Illustration of a cloud syncing wirelessly with a laptop" style="left:394px;top:440px;width:262px;height:90px;border-radius:40px 10px 6px 30px;background:linear-gradient(90deg,#5aaed6 0%,#3d8fc0 38%,#f3f3f3 48%,#cfd8de 72%,#555 100%)"></div>

<div class="soft-rule" style="top:571px"></div>

<div class="art" role="img" aria-label="Illustration of a laptop in front of a globe wrapped in clouds" style="left:70px;top:602px;width:205px;height:142px;border-radius:70px 70px 8px 8px;background:linear-gradient(135deg,#e8a5d8 0%,#9cc7ee 40%,#5fa0d8 65%,#e9eef3 100%)"></div>
<h3 class="feature-title" style="left:290px;top:620px">Why Us?</h3>
<div class="feature-text" style="left:290px;top:643px;width:370px">
  <p>Phasellus felis dolor, scelerisque a, tempus eget, lobortis id, libero. Donec scelerisque leo ac risus. Praesent sit amet est. In dictum, dolor eu dictum porttitor, enim felis viverra mi, eget luctus massa purus quis odio. Etiam nulla massa, pharetra facilisis, volutpat in, imperdiet sit amet, sem. Aliquam nec erat at purus cursus interdum</p>
  <p>Vestibulum ligula augue, bibendum accumsan, vestibulum ut, commodo a, mi. Morbi ornare gravida elit. Integer congue, augue et malesuada iaculis, ipsum dui aliquet felis</p>
</div>

<div class="soft-rule" style="top:771px"></div>

<h3 class="col-title" style="left:58px">Benefits &amp; Services</h3>
<div class="col-text" style="left:59px">
  <p>Phasellus felis dolor, scelerisque a, tempus eget, lobortis id, libero. Donec scelerisque leo ac risus. Praesent sit amet est. In dictum dolor eu dictum porttitor, enim felis viverra mi, eget luctus</p>
  <p>Massa purus quis odio. Etiam nulla massa, pharetra facilisis, volutpat in, imperdiet sit amet, sem.</p>
</div>
<a class="btn-more" style="left:59px">READ MORE</a>

<h3 class="col-title" style="left:266px">Speed &amp; Processing</h3>
<div class="col-text" style="left:267px">
  <p>Phasellus felis dolor, scelerisque a, tempus eget, lobortis id, libero. Donec scelerisque leo ac risus. Praesent sit amet est. In dictum dolor eu dictum porttitor, enim felis viverra mi, eget luctus</p>
  <p>Massa purus quis odio. Etiam nulla massa, pharetra facilisis, volutpat in, imperdiet sit</p>
</div>
<a class="btn-more" style="left:265px">READ MORE</a>

<h3 class="col-title" style="left:468px">Why Customer Say</h3>
<div class="quote-photo" role="img" aria-label="Customer portrait photo"></div>
<p class="quote-text">Phasellus felis dolor, scelerisque a, tempus eget, lobortis id, libero. Donec scelerisque leo ac risus. Praesent sit amet est. In dictum dolor eu dictum porttitor, enim felis viverra mi</p>
<p class="quote-author">By Author Name</p>

<footer class="site-footer">
  <div class="foot-col" style="left:139px"><h4>COMPANY</h4><ul><li>Overview</li><li>Why Choose Us</li><li>How it Works</li><li>Where art clouds</li></ul></div>
  <div class="foot-sep" style="left:222px"></div>
  <div class="foot-col" style="left:249px"><h4>ABOUT US</h4><ul><li>Phasellus felis</li><li>Dolor scelerisque</li><li>Tempus eget</li><li>lobortis libero.</li></ul></div>
  <div class="foot-sep" style="left:335px"></div>
  <div class="foot-col" style="left:361px"><h4>HELP</h4><ul><li>support</li><li>Get Started</li><li>Contact Us</li></ul></div>
  <div class="foot-sep" style="left:425px"></div>
  <div class="foot-col" style="left:453px"><h4>GET IN TOUCH</h4><ul class="social"><li><i class="ico"></i>Pageboard</li><li><i class="ico"></i>Linkwell</li><li><i class="ico"></i>Chirpline</li></ul></div>
  <div class="foot-rule"></div>
  <p class="copyright">© 2013 Company Name.&nbsp; All right reserved</p>
</footer>

</body>
</html>
```